Velvet Ink Studio - Semi Permanent Makeup

Website Brief
Overview:
• Product - Cosmetics Tattooing \ Permanent Makeup
• Permanent beauty services including permanent eyebrow hairstrokes, eyeliner, lip liner, Lip Blend
• Marketing - over 18 year old women
• Website pages: Home – Services - About Rosalind – Pricing – Contact Us – Pre Procedures - Post Procedures (please read below for page titles in purple)
• There is logo and design all be done by artist hive and should be on file
Home Page
Pictures:
Logo: as per attachment
Slogan:
Special Offers:
Facebook: Setup and link on web page
Testimonials: What people are saying, Commits from clients
Marking box\Banner: that flicks around with either special offices, testimonials, location of Rosalind, slogans etc..
Services
Semi - Permanent Makeup
Eyebrows:
o Summary
o Before, After and healed pictures
Upper and Lower Eyeliner
o Summary
Lip Liner:
o Summary

Lip Blend:
o Summary
Corrections:
o Summary
Tattoo Removal:
o Summary

About Rosalind:
o Summary

Rosalind Studied Certificate:
QRTMVNP617C – Design and perform cosmetic tattooing
KMDPR719E – Maintain infection control standards in office practice setting
JPWCFE118 – Provide First Aid
Business Management - Frontline Management
Graduate Diploma - Project Management
Pricing:
Price List
Semi - Permanent Eyebrow Hairstrokes $430.00
Permanent Upper Eyeliner $420.00
Permanent Lower Eyeliner $420.00
Upper & Lower Eyeliner together $580.00
Lip Liner $360.00
Lip Blend $450.00
Tattoo Removal session $199.00
Consultation Free
• A follow-up appointment is included in all services within 4 to 6 weeks.

Aftercare Procedures Procedures:
o Summary
Contact Us:
Subscribe to mailing list:
o Email address
Contact Velvet Ink Studio:
• Name
• Phone
• Email address
• Preferred Contact Method
• Subscribe to newsletter , special offers and events
Location:
• By email: velvetinkstudio@maildrop.example
• By Phone:
o 0219374620
• Facebook: Velvet Ink Studio
• Address: 47 Fernleigh Crescent, Tui Harbour, 8093, Christchurch

Reason: I have extended the dead line as I have been working 7days a week and given that some of the communication is restricted to due to time difference. I need extra time. Thanks to all design I will be back to shortly.

Target Market(s)

Over 18 years, all ages main females, but I do get a small amount of men

Industry/Entity Type

Tattoo

Coding

Coded - Design and coding required

Number of Pages Required

5+ page

Font styles to use
Sans Serif

Requirements
Must have
• Home page
• Services page
• About Rosalind page
• Pricing – Contact Us page
• Pre Procedures - Post care procedures page
• I would client to be able to subscribe to new letter
• Please go to my facebook page - Velvet Ink Studio - Christchurch, as the banner I have here, I would like to see on my webpage
Nice to have
• Please go on to my Facebook page as there client picture that could be used Velvet Ink Studio
• Before and after pictures
• Eyeliner
• Lip Liner
• Lip Blend
• Eyebrow Hair stroke
• The first two site below are my direct competitors, so I wold like something that is better that these:
• New Zealand:
• http://www.glowinglashlines.example.nz/
• http://www.browcraftery.example.nz/

```html
<!DOCTYPE html>
<html lang="en">
<head>
<meta charset="utf-8">
<title>Velvet Ink Studio – Cosmetics Tattooing</title>
<link href="https://fonts.googleapis.com/css2?family=Dancing+Script:wght@500;700&family=Open+Sans:wght@400;600;700&display=swap" rel="stylesheet">
<style>
:root{
  --blue:#2d9ad8;
  --blue-dark:#1f7fba;
  --blue-deep:#176a9e;
  --ink:#333a40;
  --muted:#6d747a;
  --panel-dark:#3c3f43;
  --soft-grey:#e8edf1;
  --white:#ffffff;
  --nav-ink:#4c63a3;
  --rose:#b81f2e;
}
*{margin:0;padding:0;box-sizing:border-box}
html,body{width:1200px;height:2936px;overflow:hidden;background:var(--white)}
body{font-family:"Open Sans",Arial,sans-serif;color:var(--ink);font-size:13px;line-height:1.55;position:relative}
.script{font-family:"Dancing Script",cursive}
.abs{position:absolute}

/* top bar */
.topbar{position:absolute;left:0;top:0;width:1200px;height:48px;border-bottom:1px solid #eee;display:flex;align-items:center;justify-content:space-between;padding:0 80px;font-size:12px;color:var(--muted)}
.topbar .contact{display:flex;gap:28px;align-items:center}
.topbar .contact span{display:flex;gap:8px;align-items:center}
.social-dots{display:flex;gap:8px}
.social-dots i{width:22px;height:22px;border-radius:50%;background:var(--blue);display:block}
.social-dots i:nth-child(1){background:#3b5b99}
.social-dots i:nth-child(3){background:#c4302b}

/* nav */
.nav{position:absolute;left:0;top:48px;width:1200px;height:104px;display:flex;align-items:center;padding:0 72px}
.nav ul{list-style:none;display:flex;gap:34px;align-items:center}
.nav a{font-family:"Dancing Script",cursive;font-size:22px;color:var(--nav-ink);text-decoration:none}
.nav .active{background:var(--blue);color:var(--white);padding:4px 14px}
.nav .right{margin-left:auto}
.brand{position:absolute;left:600px;top:22px;transform:translateX(-50%);display:flex;flex-direction:column;align-items:center;gap:6px}
.brand i{width:30px;height:30px;border-radius:50%;background:var(--ink);display:block}
.brand span{font-family:"Dancing Script",cursive;font-size:22px;color:var(--ink)}

/* hero */
.hero{position:absolute;left:0;top:152px;width:1200px;height:620px;overflow:hidden}
.hero-photo{position:absolute;inset:0;background:radial-gradient(ellipse at 62% 40%,#f4e1dc 0%,#e9ccc4 30%,#d9b2aa 55%,#c9c2c4 80%),linear-gradient(90deg,#dedada,#ece4e1)}
.hero-photo::after{content:"";position:absolute;left:520px;top:300px;width:320px;height:220px;border-radius:50%;background:radial-gradient(circle,rgba(184,31,46,.75),rgba(184,31,46,0) 70%)}
.hero h1{position:absolute;left:88px;top:332px;font-family:"Dancing Script",cursive;font-size:56px;font-weight:700;color:var(--white);text-shadow:0 2px 6px rgba(0,0,0,.35)}
.hero .tag{position:absolute;left:88px;top:412px;background:rgba(45,154,216,.55);color:var(--white);font-family:"Dancing Script",cursive;font-size:40px;padding:0 120px 0 10px;line-height:56px}
.hero .arrows{position:absolute;left:92px;top:494px;display:flex;gap:10px}
.hero .arrows span{width:30px;height:30px;border-radius:50%;background:rgba(0,0,0,.35);display:flex;align-items:center;justify-content:center}

/* services */
.services-band{position:absolute;left:0;top:740px;width:1200px;height:260px;background:linear-gradient(180deg,#2f2c2d,#55504f 50%,#3a3536);}
.services-title{position:absolute;top:760px;width:1200px;text-align:center;font-family:"Dancing Script",cursive;font-size:46px;color:var(--white)}
.services-title::after{content:"";display:block;width:120px;height:2px;background:var(--blue);margin:2px auto 0}
.service{position:absolute;top:820px;width:240px;text-align:center}
.service .thumb{width:176px;height:176px;border-radius:50%;border:5px solid var(--white);margin:0 auto;background:radial-gradient(circle at 50% 45%,#f3ddd3,#d9b4a6 70%);box-shadow:0 2px 8px rgba(0,0,0,.3)}
.service h3{font-family:"Dancing Script",cursive;font-size:26px;color:var(--ink);margin-top:22px}
.service p{font-size:11px;color:var(--muted);line-height:1.5;margin:6px 10px 0}
.btn-dark{display:inline-block;background:var(--panel-dark);color:var(--white);font-size:11px;padding:5px 14px;margin-top:14px}

/* about */
.about-photo{position:absolute;left:88px;top:1248px;width:456px;height:280px;background:linear-gradient(135deg,#d8dadc,#bfc3c7 40%,#e6d9d2 75%,#cfc4be);border:1px solid #ddd}
.about{position:absolute;left:580px;top:1206px;width:540px}
.about h2{font-size:34px;font-weight:600;color:var(--ink);line-height:1.2}
.about h2 em{font-family:"Dancing Script",cursive;font-style:normal;color:var(--blue);font-size:40px;font-weight:500}
.about h2::after{content:"";display:block;width:70px;height:2px;background:var(--blue);margin-top:6px}
.about p{font-size:12.5px;color:var(--muted);margin-top:14px}
.btn-blue{display:inline-block;background:var(--blue);color:var(--white);font-size:11px;padding:6px 16px;margin-top:18px}

/* offers */
.offers{position:absolute;left:0;top:1580px;width:1200px;height:280px;background:var(--soft-grey)}
.offer{position:absolute;top:60px;height:200px;display:flex}
.offer .photo{width:176px;height:200px;background:linear-gradient(160deg,#c8d6e0,#9fb6c6 60%,#d6c9c2)}
.offer .body{flex:1;background:var(--blue);color:var(--white);padding:18px 22px}
.offer h3{font-family:"Dancing Script",cursive;font-size:34px;font-weight:500;line-height:1.1}
.offer p{font-size:11.5px;margin-top:8px;line-height:1.5;opacity:.95}
.offer .more{font-size:11px;font-weight:700;margin-top:10px;display:inline-block}

/* booking */
.booking-title{position:absolute;left:88px;top:1922px;font-family:"Dancing Script",cursive;font-size:40px;color:var(--blue)}
.calendar{position:absolute;left:88px;top:1988px;width:304px;height:296px;background:var(--blue)}
.calendar .head{display:flex;justify-content:space-between;align-items:center;height:40px;padding:0 14px;color:var(--white);font-size:12px;font-weight:700;background:var(--blue-dark)}
.calendar table{width:100%;border-collapse:collapse;color:var(--white);font-size:12px;text-align:center}
.calendar th{height:34px;font-weight:700}
.calendar td{height:42px;border:1px solid rgba(255,255,255,.25)}
.calendar td.today{background:var(--white);color:var(--blue);font-weight:700}
.book-now{position:absolute;left:400px;top:1988px;width:300px;height:296px;background:var(--panel-dark);padding:16px 20px;color:var(--white)}
.book-now h3{font-family:"Dancing Script",cursive;font-size:26px;font-weight:500;margin-bottom:10px}
.field{background:var(--white);height:30px;margin-bottom:10px;font-size:11px;color:#999;padding:6px 10px}
.field.area{height:46px}
.book-now .btn-blue{margin-top:2px}
.newsletter{position:absolute;left:728px;top:1988px;width:400px;height:296px;background:var(--blue);padding:8px}
.newsletter .frame{border:1px solid rgba(255,255,255,.7);height:100%;padding:16px 20px;color:var(--white)}
.newsletter h3{font-family:"Dancing Script",cursive;font-size:32px;font-weight:500}
.newsletter p{font-size:11.5px;margin:6px 0 16px}
.newsletter .btn-sub{display:inline-block;background:var(--panel-dark);color:var(--white);font-size:12px;padding:7px 20px}

/* testimonials */
.testi-title{position:absolute;top:2368px;width:1200px;text-align:center;font-family:"Dancing Script",cursive;font-size:40px;color:var(--ink)}
.testi-title::after{content:"";display:block;width:80px;height:2px;background:var(--blue);margin:2px auto 0}
.testimonial{position:absolute;top:2460px;width:450px;display:flex;gap:20px}
.testimonial .avatar{width:92px;height:92px;border-radius:50%;flex:none;background:radial-gradient(circle at 50% 40%,#f1dcd2,#cfae9f 75%);border:3px solid #eee}
.testimonial p{font-size:11.5px;color:var(--muted)}
.testimonial b{display:block;color:var(--blue);font-size:12px;margin-top:8px}
.testimonial small{font-size:11px;color:var(--muted)}
.t-arrow{position:absolute;top:2490px}

/* footer */
.footer{position:absolute;left:0;top:2656px;width:1200px;height:228px;background:var(--blue);color:var(--white)}
.fcol{position:absolute;top:32px;width:260px;font-size:11.5px;line-height:1.6}
.fcol h4{font-family:"Dancing Script",cursive;font-size:22px;font-weight:500;margin-bottom:8px}
.fcol .row{display:flex;gap:8px;align-items:flex-start;margin-bottom:6px}
.social-squares{display:flex;gap:10px;margin-top:6px}
.social-squares i{width:30px;height:30px;background:var(--white);display:block}
.bottom-bar{position:absolute;left:0;top:2884px;width:1200px;height:52px;background:var(--blue-deep);color:var(--white);font-size:11px;display:flex;align-items:center;justify-content:center}
</style>
</head>
<body>

<header class="topbar">
  <div class="contact">
    <span><svg width="12" height="12" viewBox="0 0 24 24"><path fill="#2d9ad8" d="M6.6 10.8a15 15 0 006.6 6.6l2.2-2.2c.3-.3.7-.4 1-.2 1.1.4 2.3.6 3.6.6.6 0 1 .4 1 1V20c0 .6-.4 1-1 1A17 17 0 013 4c0-.6.4-1 1-1h3.5c.6 0 1 .4 1 1 0 1.3.2 2.5.6 3.6.1.3 0 .7-.2 1z"/></svg>+1 555 014 2297</span>
    <span><svg width="13" height="10" viewBox="0 0 26 20"><rect x="1" y="1" width="24" height="18" fill="none" stroke="#2d9ad8" stroke-width="2"/><path d="M1 1l12 10L25 1" fill="none" stroke="#2d9ad8" stroke-width="2"/></svg>hello@velvetink.example</span>
  </div>
  <div class="social-dots"><i></i><i></i><i></i></div>
</header>

<nav class="nav">
  <ul>
    <li><a class="active">Home</a></li>
    <li><a>Services</a></li>
    <li><a>About Rosalind</a></li>
    <li><a>Pricing</a></li>
  </ul>
  <div class="brand"><i></i><span>Velvet Ink Studio</span></div>
  <ul class="right">
    <li><a>Pre Procedures</a></li>
    <li><a>Post Procedures</a></li>
    <li><a>Contact Us</a></li>
  </ul>
</nav>

<section class="hero">
  <div class="hero-photo" role="img" aria-label="Portrait of a woman with defined permanent makeup holding red roses"></div>
  <h1>Cosmetics Tattooing</h1>
  <div class="tag">Permanent Makeup</div>
  <div class="arrows">
    <span><svg width="10" height="12" viewBox="0 0 10 12"><path d="M7 1L2 6l5 5" fill="none" stroke="#fff" stroke-width="2"/></svg></span>
    <span><svg width="10" height="12" viewBox="0 0 10 12"><path d="M3 1l5 5-5 5" fill="none" stroke="#fff" stroke-width="2"/></svg></span>
  </div>
  <svg class="abs" style="left:0;top:520px" width="1200" height="100" viewBox="0 0 1200 100" preserveAspectRatio="none"><path d="M0 0 Q600 150 1200 0 L1200 100 L0 100Z" fill="#2f2c2d"/></svg>
</section>

<div class="services-band" role="img" aria-label="Dark close-up of eyes with permanent eyeliner"></div>
<svg class="abs" style="left:0;top:940px" width="1200" height="60" viewBox="0 0 1200 60" preserveAspectRatio="none"><path d="M0 60 Q600 -20 1200 60Z" fill="#fff"/></svg>
<h2 class="services-title">Our Services</h2>

<div class="service" style="left:90px"><div class="thumb" role="img" aria-label="Eyebrow hairstroke treatment"></div><h3>Eyebrow Hairstrokes</h3><p>Natural looking brows drawn stroke by stroke to frame your face and save time every morning.</p><span class="btn-dark">Read more</span></div>
<div class="service" style="left:350px"><div class="thumb" role="img" aria-label="Eyeliner treatment"></div><h3>Eyeliner</h3><p>Soft or defined upper and lower lines that stay put through swimming, sport and long days.</p><span class="btn-dark">Read more</span></div>
<div class="service" style="left:610px"><div class="thumb" role="img" aria-label="Lip liner treatment"></div><h3>Lip Liner</h3><p>A subtle outline that adds shape and balance to your lips without daily pencil touch ups.</p><span class="btn-dark">Read more</span></div>
<div class="service" style="left:870px"><div class="thumb" role="img" aria-label="Lip blend treatment"></div><h3>Lip Blend</h3><p>Full colour softly blended across the lips for a fresh, even tone that lasts for years.</p><span class="btn-dark">Read more</span></div>

<div class="about-photo" role="img" aria-label="Artist performing a cosmetic tattoo procedure on a client"></div>
<section class="about">
  <h2>About <em>Rosalind</em></h2>
  <p>Rosalind has spent many years perfecting the craft of cosmetic tattooing, combining careful technique with a gentle, caring approach. Every treatment begins with a relaxed consultation to understand your features, colouring and lifestyle so the result looks natural and suits you perfectly. She works in a calm private studio with strict hygiene standards.</p>
  <p>Qualified in cosmetic tattooing, infection control and first aid, she keeps learning new methods and pigments so clients always enjoy safe, modern and lasting results they love.</p>
  <span class="btn-blue">Read More</span>
</section>

<section class="offers">
  <div class="offer" style="left:72px;width:496px"><div class="photo" role="img" aria-label="Client relaxing during a treatment"></div><div class="body"><h3>Special Offers 1</h3><p>Book a brow hairstroke session this month and receive a complimentary lash tint with your follow-up visit. Limited places are available.</p><span class="more">Read More ›</span></div></div>
  <div class="offer" style="left:600px;width:512px"><div class="photo" role="img" aria-label="Client receiving an eyeliner treatment"></div><div class="body"><h3>Special Offers 2</h3><p>Choose upper and lower eyeliner together and save on the combined price. Free consultation included for all new clients.</p><span class="more">Read More ›</span></div></div>
</section>

<h2 class="booking-title">Booking</h2>
<div class="calendar">
  <div class="head"><span>‹</span><span>APRIL 2015</span><span>›</span></div>
  <table>
    <tr><th>M</th><th>T</th><th>W</th><th>T</th><th>F</th><th>S</th><th>S</th></tr>
    <tr><td></td><td></td><td>1</td><td>2</td><td>3</td><td>4</td><td>5</td></tr>
    <tr><td>6</td><td>7</td><td>8</td><td>9</td><td>10</td><td>11</td><td>12</td></tr>
    <tr><td>13</td><td>14</td><td>15</td><td>16</td><td>17</td><td>18</td><td>19</td></tr>
    <tr><td class="today">20</td><td>21</td><td>22</td><td>23</td><td>24</td><td>25</td><td>26</td></tr>
    <tr><td>27</td><td>28</td><td>29</td><td>30</td><td></td><td></td><td></td></tr>
  </table>
</div>
<div class="book-now">
  <h3>Book Now</h3>
  <div class="field">Name</div>
  <div class="field">Phone</div>
  <div class="field">Email</div>
  <div class="field area">Message</div>
  <span class="btn-blue">Submit</span>
</div>
<div class="newsletter"><div class="frame">
  <h3>Newsletter Subscribe</h3>
  <p>Join our mailing list for news, special offers and upcoming events straight to your inbox.</p>
  <div class="field">Name</div>
  <div class="field">Enter your email address</div>
  <span class="btn-sub">Subscribe</span>
</div></div>

<h2 class="testi-title">Testimonials</h2>
<svg class="t-arrow" style="left:60px" width="14" height="22" viewBox="0 0 14 22"><path d="M11 2L3 11l8 9" fill="none" stroke="#bbb" stroke-width="2"/></svg>
<div class="testimonial" style="left:120px"><div class="avatar" role="img" aria-label="Client portrait"></div><div><p>My brows look so natural that friends cannot tell they are tattooed. The whole visit was calm and professional.</p><b>Amelia Grant</b><small>Marketing Executive</small></div></div>
<div class="testimonial" style="left:640px"><div class="avatar" role="img" aria-label="Client portrait"></div><div><p>I wake up with perfect eyeliner every day now. Rosalind explained every step and made me feel at ease.</p><b>Harper Lane</b><small>Marketing Executive</small></div></div>
<svg class="t-arrow" style="left:1126px" width="14" height="22" viewBox="0 0 14 22"><path d="M3 2l8 9-8 9" fill="none" stroke="#bbb" stroke-width="2"/></svg>

<footer class="footer">
  <div class="fcol" style="left:80px;width:240px">
    <h4>Contact</h4>
    <div class="row"><svg width="10" height="14" viewBox="0 0 10 14"><path d="M5 0a5 5 0 00-5 5c0 4 5 9 5 9s5-5 5-9a5 5 0 00-5-5zm0 7a2 2 0 110-4 2 2 0 010 4z" fill="#fff"/></svg><span>47 Fernleigh Crescent,<br>Tui Harbour, 8093</span></div>
    <div class="row"><svg width="12" height="12" viewBox="0 0 24 24"><path fill="#fff" d="M6.6 10.8a15 15 0 006.6 6.6l2.2-2.2c.3-.3.7-.4 1-.2 1.1.4 2.3.6 3.6.6.6 0 1 .4 1 1V20c0 .6-.4 1-1 1A17 17 0 013 4c0-.6.4-1 1-1h3.5c.6 0 1 .4 1 1 0 1.3.2 2.5.6 3.6.1.3 0 .7-.2 1z"/></svg><span>(+400) 555-0173</span></div>
    <div class="row"><svg width="13" height="10" viewBox="0 0 26 20"><rect x="1" y="1" width="24" height="18" fill="none" stroke="#fff" stroke-width="2"/><path d="M1 1l12 10L25 1" fill="none" stroke="#fff" stroke-width="2"/></svg><span>studio@velvetink.example</span></div>
  </div>
  <div class="fcol" style="left:352px">
    <h4>Latest Tweets</h4>
    <div class="row"><span>›</span><span>New brow appointments open for next month, book early to secure a spot.</span></div>
    <div class="row"><span>›</span><span>Healed lip blend results from this week, soft colour and lovely shape.</span></div>
  </div>
  <div class="fcol" style="left:660px;width:260px">
    <h4>Neque porro quisquam</h4>
    <p>Every treatment includes a follow-up appointment within four to six weeks to perfect colour and shape.</p>
    <p style="margin-top:8px">Read our pre and post care guides before your visit for the best results.</p>
  </div>
  <div class="fcol" style="left:960px;width:180px">
    <h4>Social Media</h4>
    <div class="social-squares"><i></i><i></i><i></i></div>
  </div>
</footer>
<div class="bottom-bar">2015 All Rights Reserved</div>

</body>
</html>
```